Business Card Design Project

Our organization is in need of a business card design with the use of our logo. We are looking for professional design that will embellish the image our consulting firm.

Here is a summary of what we do: Quorvent is systems consulting firm that specializes in the management, migration, and maintenance of IT infrastructure solutions.

Here is a link to my website: http://quorvent-example.com

I have attached the logo.

Target Market(s)

Organization that need IT and server support.

Industry/Entity Type

Business

```html
<!DOCTYPE html>
<html lang="en">
<head>
<meta charset="utf-8">
<title>Quorvent — Business Card</title>
<link href="https://fonts.googleapis.com/css2?family=Jost:wght@400;500&display=swap" rel="stylesheet">
<style>
  :root {
    --navy: #1d2758;
    --navy-deep: #18214c;
    --orange: #e0631e;
    --card-white: #eef0f2;
    --ink: #1f2a55;
    --backdrop: #dedad3;
    --glow: rgba(120, 140, 200, 0.28);
  }
  * { margin: 0; padding: 0; box-sizing: border-box; }
  html, body {
    width: 1200px; height: 879px; overflow: hidden;
    background: var(--backdrop);
    font-family: "Jost", "Futura", sans-serif;
  }
  .stage {
    position: relative; width: 1200px; height: 879px;
    display: flex; align-items: center; justify-content: center; gap: 50px;
  }
  .card {
    position: relative; width: 520px; height: 297px;
    box-shadow: 0 6px 18px rgba(0,0,0,0.18);
  }
  /* Front */
  .card-front { background: var(--card-white); color: var(--ink); }
  .brand {
    position: absolute; left: 36px; top: 40px;
    display: flex; align-items: center; gap: 16px;
  }
  .brand-dot { width: 40px; height: 40px; border-radius: 50%; background: var(--navy); }
  .brand-name { font-size: 38px; font-weight: 400; color: var(--navy); letter-spacing: 0.5px; }
  .contact-list {
    position: absolute; left: 36px; top: 150px; list-style: none;
    font-size: 13.5px; line-height: 19px;
  }
  .contact-list li { display: flex; align-items: center; gap: 8px; }
  .contact-list svg { width: 11px; height: 11px; fill: var(--navy); flex: none; }
  .contact-rule {
    position: absolute; left: 36px; top: 233px; width: 290px; height: 2px;
    background: var(--orange);
  }
  .address {
    position: absolute; left: 36px; top: 243px; font-size: 14px;
    display: flex; align-items: center; gap: 7px;
  }
  .address svg { width: 11px; height: 14px; fill: var(--navy); }
  .person { position: absolute; right: 36px; top: 140px; text-align: right; }
  .person-name { font-size: 24px; color: var(--orange); font-weight: 400; }
  .person-role { font-size: 13.5px; color: var(--ink); margin-top: 2px; }
  /* Back */
  .card-back { background: var(--navy); overflow: hidden; }
  .back-glow {
    position: absolute; inset: 0;
    background: radial-gradient(circle at 72% 62%, var(--glow) 0%, rgba(0,0,0,0) 55%);
  }
  .back-name {
    position: absolute; left: 0; right: 0; top: 100px; text-align: center;
    font-size: 58px; color: #ffffff; font-weight: 400; letter-spacing: 1px;
  }
  .back-url {
    position: absolute; left: 40px; bottom: 32px;
    font-size: 13.5px; color: #ffffff; letter-spacing: 2px;
  }
</style>
</head>
<body>
<main class="stage">
  <section class="card card-front" aria-label="Business card front">
    <div class="brand">
      <span class="brand-dot"></span>
      <span class="brand-name">Quorvent</span>
    </div>
    <ul class="contact-list">
      <li><svg viewBox="0 0 12 12"><rect x="3" y="0" width="6" height="12" rx="1.2"/></svg>555.014.2210</li>
      <li><svg viewBox="0 0 12 12"><rect x="3" y="0" width="6" height="4"/><rect x="0" y="4" width="12" height="6" rx="1"/></svg>555.014.2211</li>
      <li><svg viewBox="0 0 12 12"><rect x="0" y="2" width="12" height="8" rx="1.5"/></svg>name.surname@quorvent-example.com</li>
      <li><svg viewBox="0 0 12 12"><circle cx="6" cy="6" r="5.5"/></svg>www.quorvent-example.com</li>
    </ul>
    <div class="contact-rule"></div>
    <div class="address">
      <svg viewBox="0 0 12 16"><path d="M6 0a6 6 0 0 0-6 6c0 4.5 6 10 6 10s6-5.5 6-10a6 6 0 0 0-6-6zm0 8.5A2.5 2.5 0 1 1 6 3.5a2.5 2.5 0 0 1 0 5z"/></svg>
      4120 Ridgeline Pkwy, Fairhaven, TX 75001
    </div>
    <div class="person">
      <p class="person-name">Name Surname</p>
      <p class="person-role">manager/CEO</p>
    </div>
  </section>

  <section class="card card-back" aria-label="Business card back">
    <div class="back-glow" role="img" aria-label="Soft decorative glow in navy tones"></div>
    <p class="back-name">Quorvent</p>
    <p class="back-url">www.quorvent-example.com</p>
  </section>
</main>
</body>
</html>
```